Software Company Requires Website

We need a web design for a new mobile software development company based in London named Velquin Solutions.
The design needs to be clean and smooth. Not too flashy, not too boring.
I would like to try the design with some warm colors, and maybe a headline or something highlighted with a strong color. ( logo ? ) The layout should be something like the bellow links, all in one page.

http://brantelo.net/
http://www.kelvory.com/
http://www.work-plover.de/
http://www.tusker.com/
http://www.quildenta.com/us/

Now some of them they seem different from the others, but in each of them there is something that ticks my brain, so it`s up to you to surprise me.

I have uploaded the logo of the company, so you guys can fit that in your design as well.
Updates

Hy everybody This will be the last update for the brief. The company will focus in the beginning for mobile development only, so i would like the website design to be done in a matter that will reflect that. We will develop IOS, Android and Windows applications. We will also require 3 pages: One for the home menu, one for portfolio and one for contact us. The layout should be the same ( one page scroll down ) but the design of the 3 pages different. Please readdress the brief. Hope that i provided enough information for the scope of the project.

I have uploaded the logo that you guys can use. If the logo requires small modifications you can adjust that to suit your idea as long as the logo does not change completely.

Target Market(s)

High End companies that require simplified software solutions.

Industry/Entity Type

It Company

Number of Pages Required

3 page

Requirements
Must have
• One page scroll down layout for 3 pages:
• one for home page, one for portfolio and one for contact us.
• In the portfolio page we would like to have different display options for given examples of applications ( min 3 )

```html
<!DOCTYPE html>
<html lang="en">
<head>
<meta charset="utf-8">
<title>Velquin Solutions – Mobile Software Development</title>
<link href="https://fonts.googleapis.com/css2?family=Open+Sans:wght@300;400;600;700&display=swap" rel="stylesheet">
<style>
  :root {
    --blue: #2f78c2;
    --blue-deep: #1f5e9e;
    --blue-dark: #184d85;
    --blue-text: #2a6db3;
    --grey-bar: #f3f3f3;
    --grey-soft: #f4f6f9;
    --grey-text: #8a8a8a;
    --nav-text: #a9a9a9;
    --white: #ffffff;
    --field: rgba(18, 58, 108, 0.45);
  }
  * { box-sizing: border-box; margin: 0; padding: 0; }
  html, body { width: 1200px; height: 2191px; overflow: hidden; }
  body { font-family: "Open Sans", Arial, sans-serif; background: var(--white); position: relative; }

  /* Hero */
  .hero { position: absolute; left: 0; top: 0; width: 1200px; height: 588px;
    background: linear-gradient(180deg, #3a86d0 0%, #2c74bd 60%, #1d5a97 100%); overflow: hidden; }
  .hero-floor { position: absolute; left: 0; top: 470px; width: 1200px; height: 118px;
    background: linear-gradient(180deg, #2a6aa9 0%, #1c5186 100%); }
  .hero-brand { position: absolute; left: 171px; top: 100px; display: flex; align-items: center; gap: 22px; }
  .hero-brand .mark { width: 56px; height: 56px; border: 3px solid var(--white); }
  .hero-brand .name { font-size: 64px; font-weight: 300; color: var(--white); letter-spacing: 1px; line-height: 1; }
  .hero-tagline { position: absolute; left: 171px; top: 268px; width: 600px; font-size: 25px; font-weight: 300;
    color: var(--white); line-height: 1.3; text-transform: uppercase; }
  .hero-cta { position: absolute; left: 171px; top: 375px; width: 286px; height: 51px;
    background: rgba(20, 60, 110, 0.35); color: var(--white); font-size: 25px; font-weight: 300;
    display: flex; align-items: center; justify-content: center; gap: 20px; text-transform: uppercase; }
  .hero-scroll { position: absolute; left: 176px; top: 500px; }
  .hero-device { position: absolute; left: 790px; top: 65px; width: 320px; height: 470px; border-radius: 40px;
    background: radial-gradient(ellipse at 50% 50%, rgba(240,242,245,0.9) 0%, rgba(214,219,226,0.7) 50%, rgba(210,215,222,0) 72%); }

  /* Navigation */
  .nav { position: absolute; left: 0; top: 588px; width: 1200px; height: 69px; background: var(--grey-bar); }
  .nav a { position: absolute; top: 25px; font-size: 13px; color: var(--nav-text); text-decoration: none; text-transform: uppercase; }
  .nav a.is-active { color: var(--blue-text); font-weight: 700; }
  .nav-brand { position: absolute; left: 545px; top: 22px; display: flex; align-items: center; gap: 7px; }
  .nav-brand .mark { width: 14px; height: 14px; border: 2px solid var(--blue-text); }
  .nav-brand .name { font-size: 16px; font-weight: 600; color: var(--blue-text); }

  /* Section headings */
  .section-title { position: absolute; left: 0; width: 1200px; text-align: center; font-size: 38px;
    font-weight: 400; color: var(--blue-text); text-transform: uppercase; line-height: 1; }
  .title-rule { position: absolute; left: 458px; width: 284px; height: 5px;
    border-top: 1px solid var(--blue-text); border-bottom: 1px solid var(--blue-text); }

  /* About */
  .about { position: absolute; left: 0; top: 657px; width: 1200px; height: 334px; background: var(--white); }
  .about p { position: absolute; left: 209px; width: 782px; text-align: center; font-size: 11.5px;
    line-height: 16px; color: var(--grey-text); }

  /* Portfolio */
  .portfolio { position: absolute; left: 0; top: 991px; width: 1200px; height: 526px; background: var(--grey-soft); }
  .portfolio-grid { position: absolute; left: 171px; top: 127px; width: 858px; height: 346px;
    display: grid; grid-template-columns: repeat(3, 286px); grid-template-rows: repeat(2, 173px); }
  .work-tile { position: relative; }
  .work-tile.tone-a { background: radial-gradient(circle at 50% 50%, #dfe6ee 0%, #eceef0 70%); }
  .work-tile.tone-b { background: radial-gradient(circle at 60% 60%, #d6dde6 0%, #f0f1f3 70%); }
  .work-tile.tone-c { background: radial-gradient(circle at 50% 55%, #e6dcc6 0%, #eef0f2 70%); }
  .work-tile.tone-d { background: radial-gradient(circle at 50% 55%, #d7d7d9 0%, #e6e7e9 70%); }
  .work-tile.featured { background: var(--blue); display: flex; flex-direction: column; align-items: center; }
  .featured .plus { margin-top: 28px; }
  .featured h3 { margin-top: 10px; font-size: 18px; font-weight: 700; color: var(--white); text-transform: uppercase; letter-spacing: 0.3px; }
  .featured .read-more { margin-top: 10px; width: 118px; height: 29px; background: #d9e4ef; color: var(--blue-text);
    font-size: 12px; font-weight: 600; display: flex; align-items: center; justify-content: center; text-transform: uppercase; }

  /* Quote form */
  .quote { position: absolute; left: 0; top: 1517px; width: 1200px; height: 442px;
    background: linear-gradient(180deg, #2d6fb2 0%, #2a69a9 100%); }
  .quote h2 { position: absolute; left: 250px; top: 56px; width: 700px; text-align: center; font-size: 38px;
    font-weight: 300; color: var(--white); line-height: 46px; text-transform: uppercase; }
  .field { position: absolute; background: var(--field); color: var(--white); font-size: 12px; font-weight: 600;
    padding: 14px 0 0 16px; text-transform: uppercase; }
  .field.name { left: 175px; top: 161px; width: 279px; height: 45px; }
  .field.phone { left: 458px; top: 161px; width: 279px; height: 45px; }
  .field.email { left: 742px; top: 161px; width: 281px; height: 45px; }
  .field.message { left: 175px; top: 211px; width: 848px; height: 106px; }
  .field.message svg { position: absolute; right: 4px; bottom: 4px; }
  .send { position: absolute; left: 439px; top: 344px; width: 320px; height: 50px; background: var(--white);
    border-bottom: 5px solid #8fb6de; border-radius: 3px; color: var(--blue-text); font-size: 17px;
    display: flex; align-items: center; justify-content: center; text-transform: uppercase; }

  /* Contact bar */
  .contact-bar { position: absolute; left: 0; top: 1959px; width: 1200px; height: 110px; background: var(--grey-bar); }
  .contact-item { position: absolute; top: 50px; display: flex; align-items: center; gap: 8px; font-size: 13px; color: #6e6e6e; }

  /* Footer */
  .footer { position: absolute; left: 0; top: 2069px; width: 1200px; height: 122px; background: var(--white); }
  .footer-brand { position: absolute; left: 0; width: 1200px; top: 18px; display: flex; justify-content: center; align-items: center; gap: 7px; }
  .footer-brand .mark { width: 14px; height: 14px; border: 2px solid var(--blue-text); }
  .footer-brand .name { font-size: 16px; font-weight: 600; color: var(--blue-text); }
  .copyright { position: absolute; left: 0; width: 1200px; top: 56px; text-align: center; font-size: 12px; color: #6e6e6e; text-transform: uppercase; }
  .social { position: absolute; left: 550px; top: 84px; display: flex; gap: 10px; }
  .social span { width: 17px; height: 17px; border-radius: 50%; background: #c5c5c5; }
  .social span.is-primary { background: var(--blue-text); }
</style>
</head>
<body>

<header class="hero">
  <div class="hero-floor" role="img" aria-label="Blue painted wooden floor planks"></div>
  <div class="hero-brand">
    <span class="mark"></span>
    <span class="name">Velquin Solutions</span>
  </div>
  <p class="hero-tagline">Mobile software development company based in London.</p>
  <div class="hero-cta">Contact Velquin
    <svg width="22" height="22" viewBox="0 0 22 22"><path d="M11 1v20M1 11h20" stroke="#fff" stroke-width="2"/></svg>
  </div>
  <svg class="hero-scroll" width="46" height="22" viewBox="0 0 46 22"><path d="M2 2l21 17L44 2" fill="none" stroke="#fff" stroke-width="2.5"/></svg>
  <div class="hero-device" role="img" aria-label="Smartphone unzipping with colourful app icons flying out"></div>
</header>

<nav class="nav">
  <a class="is-active" style="left:211px" href="#">Home</a>
  <a style="left:348px" href="#">Portfolio</a>
  <div class="nav-brand"><span class="mark"></span><span class="name">Velquin</span></div>
  <a style="left:775px" href="#">Portfolio</a>
  <a style="left:920px" href="#">Contact Us</a>
</nav>

<section class="about">
  <h2 class="section-title" style="top:47px">About</h2>
  <div class="title-rule" style="top:89px"></div>
  <p style="top:125px">Velquin Solutions builds mobile apps for phones and tablets, shaped around the way busy teams really work. We start with a short discovery phase, map the goals of each client, then design clear screens that stay simple under daily pressure. Our London studio keeps design, code and testing in one room, so ideas move fast and nothing is lost between stages. Every release is measured, tuned and supported long after launch, giving high end companies software that feels light, quick and reliable on every device they use.</p>
  <p style="top:210px">From first sketch to store listing we handle each step with care. Our small team works closely with yours, sharing progress every week and keeping plans open and honest. The result is a focused app that solves one problem well, looks calm and clean, and grows easily as your business and your users grow with it.</p>
</section>

<section class="portfolio">
  <h2 class="section-title" style="top:49px">Portfolio</h2>
  <div class="title-rule" style="top:91px"></div>
  <div class="portfolio-grid">
    <div class="work-tile tone-a" role="img" aria-label="Smartphone surrounded by a ring of app icons"></div>
    <div class="work-tile tone-b" role="img" aria-label="App icons streaming out of a smartphone screen"></div>
    <div class="work-tile tone-c" role="img" aria-label="Question-mark shaped bookshelf filled with books"></div>
    <div class="work-tile tone-d" role="img" aria-label="Laptop with web shop building blocks"></div>
    <div class="work-tile featured">
      <svg class="plus" width="40" height="40" viewBox="0 0 40 40"><path d="M20 2v36M2 20h36" stroke="#fff" stroke-width="2"/></svg>
      <h3>Lorem Ipsum Dolor</h3>
      <div class="read-more">Read More</div>
    </div>
    <div class="work-tile tone-a" role="img" aria-label="Smartphone surrounded by a ring of app icons"></div>
  </div>
</section>

<section class="quote">
  <h2>Leave your request and get the quote</h2>
  <div class="field name">Name</div>
  <div class="field phone">Telephone</div>
  <div class="field email">Email</div>
  <div class="field message">Message
    <svg width="14" height="14" viewBox="0 0 14 14"><path d="M2 13L13 2M7 13l6-6" stroke="#cfe0f1" stroke-width="1"/></svg>
  </div>
  <div class="send">Send</div>
</section>

<section class="contact-bar">
  <div class="contact-item" style="left:252px">
    <svg width="15" height="15" viewBox="0 0 16 16"><path d="M3 1l3 3-1.5 2a9 9 0 0 0 5.5 5.5L12 10l3 3-2 2C7 15 1 9 1 3z" fill="#2a6db3"/></svg>
    <span>10 20 30 40 50</span>
  </div>
  <div class="contact-item" style="left:504px">
    <svg width="14" height="16" viewBox="0 0 14 18"><path d="M7 1a6 6 0 0 1 6 6c0 4-6 10-6 10S1 11 1 7a6 6 0 0 1 6-6z" fill="#2a6db3"/><circle cx="7" cy="7" r="2.2" fill="#f3f3f3"/></svg>
    <span>45, Sample Road, LONDON</span>
  </div>
  <div class="contact-item" style="left:797px">
    <svg width="16" height="12" viewBox="0 0 16 12"><rect x="0.75" y="0.75" width="14.5" height="10.5" fill="none" stroke="#2a6db3" stroke-width="1.5"/><path d="M1 1l7 6 7-6" fill="none" stroke="#2a6db3" stroke-width="1.5"/></svg>
    <span>info@velquinsolutions.com</span>
  </div>
</section>

<footer class="footer">
  <div class="footer-brand"><span class="mark"></span><span class="name">Velquin</span></div>
  <p class="copyright">© Velquin Solutions 2014</p>
  <div class="social"><span class="is-primary"></span><span></span><span></span><span></span></div>
</footer>

</body>
</html>
```